Flyer-Design für mobiles Eiscafé / KM R7 Retro Style  / Die Frohe Kutsche
Zielgruppe
Die Frohe Kutsche ist ein mobiles Eiscafe, aus dem Kaffee, Eis und Crepes angeboten werden.
Cocktails werden ebenfalls angebnoten , stellen im Moment aber nicht das Hauptaugenmerk da, daher kann dies erst einmal vernachlässigt werden. Sollte daher erst einmal nicht erwähnt werden.
Unsere Zielgruppe sind sowohl Firmen (Firmenveranstaltungen, Jubiäen, Sommerfeste etc. ) als auch Privatveranstaltungen, wobei das Hauptaugenmerk auf Hochzeiten liegt, ebenfalls natürlch Geburtstage, als auch Veranstaltungen wie Street Food Festivals, Flohmärkte etc.
Aufgabenstellung
Gerne im DIN A4 Format, so dass es als PDF im Anhang mit versandt werden kann.
Es soll als Flyer ebenfalls als Handout durchgehen und soll an die Unternehmen der Stadt verteilt werden.
Textlich recht offen - sollte selbstverständlich die Unternehmensdaten beinhalten, ansonsten liegt das Haupaugenmerk auf einen hochwertigem Design, das die extravaganz der Dienstleistung hervorhebt.
Weniger Text ist meines erachtens mehr, wer die Kontaktdaten einsehen möchte, der findet Sie auf dem Flyer, auch wenn Sie klein sind.
Gerne mit Tafeloptik, das passt zur Tafel am Kasti.
Stellt euch vor, Ihr würdet ein Hochzeitspaar ansprechen, das ist fein gekleidet, alle Personen sind Schick bei der Veranstaltung, dazu sollte der Flyer passen.
Im Mittelpunkt soll der Kasti stehen (Frostina), dann der Eismann und Barista - Gerd und gemeinsam sind Sie
'Die Frohe Kutsche' (on Tour).

```html
<!DOCTYPE html>
<html lang="de">
<head>
<meta charset="utf-8">
<title>Die Frohe Kutsche – Flyer</title>
<link rel="stylesheet" href="https://fonts.googleapis.com/css2?family=Della+Respira&family=Dancing+Script:wght@600&family=Special+Elite&family=Montserrat:wght@400;700&display=swap">
<style>
  :root {
    --page: #e4e4e2;
    --chalk-dark: #1e1e1e;
    --chalk-mid: #2e2e2e;
    --chalk-white: #f1f1ee;
    --sky: #4aa8d8;
    --sky-band: #3fa3d6;
    --photo-frame: #ffffff;
  }
  * { margin: 0; padding: 0; box-sizing: border-box; }
  html, body { width: 1200px; height: 1200px; overflow: hidden; background: var(--page); }
  .canvas { position: relative; width: 1200px; height: 1200px; }

  .flyer {
    position: absolute; top: 250px; width: 495px; height: 700px;
    background: radial-gradient(ellipse at 45% 40%, var(--chalk-mid) 0%, var(--chalk-dark) 75%);
    box-shadow: 0 3px 10px rgba(0,0,0,.35);
    overflow: hidden;
  }
  .flyer--intro { left: 71px; }
  .flyer--offer { left: 632px; }

  .abs { position: absolute; }
  .centered { left: 0; right: 0; text-align: center; }

  .tagline {
    top: 26px; font-family: "Della Respira", serif; font-size: 16px;
    letter-spacing: 2.2px; color: var(--sky); white-space: nowrap;
  }
  .divider { top: 62px; left: 67px; width: 363px; height: 16px; }

  .ornament-row {
    height: 18px; background: rgba(241,241,238,.14); border-radius: 9px;
  }

  .photo { border: 5px solid var(--photo-frame); }
  .photo--van-small { left: 109px; top: 129px; width: 147px; height: 105px;
    background: linear-gradient(180deg, #9cc6e0 0%, #3a9cc8 55%, #4d4b47 100%); }
  .photo--host { left: 302px; top: 129px; width: 87px; height: 105px; border-bottom-width: 12px;
    background: linear-gradient(180deg, #7b7772 0%, #c99a82 45%, #1d1d1f 100%); }

  .intro-title {
    top: 94px; font-family: "Dancing Script", cursive; font-size: 21px; color: var(--chalk-white);
  }
  .caption {
    font-family: "Special Elite", monospace; font-size: 14px; color: var(--chalk-white);
    letter-spacing: 1px; text-align: center;
  }
  .caption--van { left: 109px; width: 147px; top: 244px; }
  .caption--host { left: 302px; width: 87px; top: 244px; }

  .van-illustration {
    left: 78px; top: 282px; width: 296px; height: 165px; border-radius: 30px 40px 12px 12px;
    background: linear-gradient(180deg, #f2f2f2 0%, #f2f2f2 14%, #4ab5dc 16%, #3aa8d3 75%, #2a2a2a 100%);
  }
  .brand-mark {
    font-family: "Special Elite", monospace; color: var(--chalk-white); text-align: center;
    line-height: 1.2; white-space: nowrap;
  }
  .brand-mark--intro { left: 384px; top: 290px; width: 96px; font-size: 14px; }
  .brand-mark--offer { left: 160px; top: 112px; width: 175px; font-size: 22px; }

  .equation {
    top: 458px; font-family: "Special Elite", monospace; font-size: 14px; letter-spacing: 1.3px;
    color: var(--chalk-white); white-space: nowrap;
  }
  .headline {
    top: 530px; font-family: "Dancing Script", cursive; font-size: 38px; color: var(--chalk-white);
  }
  .occasions {
    top: 583px; font-family: "Della Respira", serif; font-size: 16px; line-height: 20px;
    letter-spacing: 2.4px; color: var(--sky);
  }

  .contact-band {
    left: 26px; top: 654px; width: 440px; height: 18px;
    background: var(--sky-band);
    clip-path: polygon(0 50%, 2% 0, 98% 0, 100% 50%, 98% 100%, 2% 100%);
    font-family: "Montserrat", sans-serif; font-size: 7.6px; line-height: 18px; color: #fff;
    text-align: center; white-space: nowrap;
  }
  .contact-band strong { font-weight: 700; }
  .baseline { left: 35px; top: 679px; width: 422px; height: 0; border-top: 1px solid rgba(241,241,238,.45); }

  .photo--barista { left: 67px; top: 237px; width: 169px; height: 198px;
    background: linear-gradient(160deg, #c7d6e4 0%, #8a8f95 40%, #222 75%, #3aa8d3 100%); }
  .photo--icecream { left: 254px; top: 237px; width: 170px; height: 198px;
    background: linear-gradient(150deg, #8c8c8c 0%, #d8cfb4 35%, #6c3b6a 55%, #ece3c3 80%); }

  .promise {
    top: 456px; font-family: "Della Respira", serif; font-size: 17px; line-height: 21px;
    letter-spacing: 2.4px; color: var(--sky);
  }

  .thumb { top: 561px; height: 62px; border-width: 3px; }
  .thumb--van { left: 133px; width: 85px; background: linear-gradient(180deg, #7ea6c4 0%, #3aa0cc 60%, #444 100%); }
  .thumb--crowd { left: 227px; width: 63px; background: linear-gradient(180deg, #6f8f4e 0%, #a9b18d 60%, #8f8373 100%); }
  .thumb--service { left: 299px; width: 63px; background: linear-gradient(180deg, #3aa8d3 0%, #2a3440 60%, #1e1e1e 100%); }
</style>
</head>
<body>
<main class="canvas">

  <section class="flyer flyer--intro">
    <p class="abs centered tagline">Hausgemachtes Eis- und Kaffeespezialitäten</p>
    <svg class="abs divider" viewBox="0 0 363 16" aria-hidden="true">
      <line x1="20" y1="8" x2="173" y2="8" stroke="#f1f1ee" stroke-width="1.5"/>
      <line x1="190" y1="8" x2="343" y2="8" stroke="#f1f1ee" stroke-width="1.5"/>
      <path d="M181.5 2 L187 8 L181.5 14 L176 8 Z" fill="none" stroke="#f1f1ee" stroke-width="1.3"/>
    </svg>

    <h2 class="abs centered intro-title">Wir stellen uns vor:</h2>
    <div class="abs photo photo--van-small" role="img" aria-label="Foto des hellblauen Kleinbusses Frostina mit Eistheke"></div>
    <div class="abs photo photo--host" role="img" aria-label="Porträtfoto von Gerd"></div>
    <p class="abs caption caption--van">Frostina</p>
    <p class="abs caption caption--host">Gerd</p>

    <div class="abs van-illustration" role="img" aria-label="Freigestelltes Foto des hellblauen KM R7 mit geöffneter Verkaufsklappe und Kreidetafel"></div>
    <p class="abs brand-mark brand-mark--intro">Die Frohe<br>Kutsche</p>

    <p class="abs centered equation">Frostina + Gerd = Die Frohe Kutsche auf Tour</p>
    <div class="abs ornament-row" style="left:170px; top:503px; width:156px;" role="img" aria-label="Verschnörkeltes Kreide-Ornament"></div>

    <h1 class="abs centered headline">Ideal für jedes Event –</h1>
    <p class="abs centered occasions">Hochzeiten, Firmenfeiern,<br>Geburtstage und vieles mehr ...</p>

    <p class="abs contact-band">Ihr Ansprechpartner: Gerd Kollmann // info@frohekutsche.de // 0176 52 18 70 39 // <strong>frohekutsche.de</strong></p>
    <div class="abs baseline"></div>
  </section>

  <section class="flyer flyer--offer">
    <p class="abs centered tagline">Hausgemachtes Eis- und Kaffeespezialitäten</p>
    <svg class="abs divider" viewBox="0 0 363 16" aria-hidden="true">
      <line x1="20" y1="8" x2="173" y2="8" stroke="#f1f1ee" stroke-width="1.5"/>
      <line x1="190" y1="8" x2="343" y2="8" stroke="#f1f1ee" stroke-width="1.5"/>
      <path d="M181.5 2 L187 8 L181.5 14 L176 8 Z" fill="none" stroke="#f1f1ee" stroke-width="1.3"/>
    </svg>

    <p class="abs brand-mark brand-mark--offer">Die Frohe<br>Kutsche</p>
    <div class="abs ornament-row" style="left:169px; top:197px; width:157px;" role="img" aria-label="Verschnörkeltes Kreide-Ornament"></div>

    <div class="abs photo photo--barista" role="img" aria-label="Foto von Gerd an der Siebträgermaschine beim Kaffeezubereiten"></div>
    <div class="abs photo photo--icecream" role="img" aria-label="Foto der Eistheke mit verschiedenen Eissorten in Edelstahlwannen"></div>

    <p class="abs centered promise">Wir bringen feinstes Eis und leckere<br>Kaffeespezialitäten auf deine Veranstaltung.</p>
    <div class="abs ornament-row" style="left:169px; top:516px; width:157px;" role="img" aria-label="Verschnörkeltes Kreide-Ornament"></div>

    <div class="abs photo thumb thumb--van" role="img" aria-label="Foto des Busses im Einsatz"></div>
    <div class="abs photo thumb thumb--crowd" role="img" aria-label="Foto von Gästen in der Warteschlange im Grünen"></div>
    <div class="abs photo thumb thumb--service" role="img" aria-label="Foto vom Verkauf an der Busklappe"></div>

    <p class="abs contact-band">Ihr Ansprechpartner: Gerd Kollmann // info@frohekutsche.de // 0176 52 18 70 39 // <strong>frohekutsche.de</strong></p>
    <div class="abs baseline"></div>
  </section>

</main>
</body>
</html>
```